Need web design for our e-assessment company

We need a web design for our e-assessment company called Tavelo. We develop modern, web-based software for supporting the testing and examination process. The application is delivered as a SaaS solution.

The application helps our customers save time and money.

The design should communicate the following:

- Modern
- Innovation
- Security
- Performance

Attached you can find a screenshot of our application as well as some thoughts on the website.

We would like a front page as well as 1 sub page.

And lastly, one more website we draw inspiration from (on top of the ones mentioned in the attached document): http://www.plonkavery.example/
Updates

Dear all,

I have updated the description with 1 more example of websites we like as well as added that we would like a front page and a sub page.

Thanks in advance.

Best regards,

Torlak

Target Market(s)

Our target groups are higher education and awarding organisations. Decision makers are mostly men age 45+.

Industry/Entity Type

It Company

Requirements
Must have
• 1 front page and 1 sub page

```html
<!DOCTYPE html>
<html lang="en">
<head>
<meta charset="utf-8">
<title>Tavelo – Assessment Made Simple</title>
<link href="https://fonts.googleapis.com/css2?family=Lato:wght@300;400;700;900&display=swap" rel="stylesheet">
<style>
:root{
  --orange:#f26a1b;
  --orange-dark:#d95a10;
  --green:#5aae2a;
  --green-dark:#43901c;
  --ink:#2d2d2d;
  --muted:#9a9a9a;
  --grey-band:#efefef;
  --line:#e2e2e2;
  --footer:#2f2f2f;
  --footer-bottom:#212121;
  --footer-text:#d6d6d6;
  --brown:#7a2f0c;
  --app-blue:#3f8bd6;
  --app-blue-dark:#2f6fb4;
  --app-side:#2a323d;
  --app-side-dark:#222932;
  --app-bg:#e9ecef;
  --teal:#2db3a6;
}
*{box-sizing:border-box;margin:0;padding:0}
html,body{width:1200px;height:2808px;overflow:hidden;background:#fff}
body{font-family:"Lato",Arial,sans-serif;color:var(--ink)}
.page{position:relative;width:1200px;height:2808px;overflow:hidden}
.abs{position:absolute}

/* hero */
.hero{position:absolute;left:0;top:0;width:1200px;height:756px;overflow:hidden;
  background:linear-gradient(180deg,#3a3d40 0%,#6b6f70 35%,#9ea3a0 70%,#c9ccc6 100%)}
.hero-photo{position:absolute;inset:0;
  background:radial-gradient(ellipse at 12% 65%,rgba(90,110,140,.55),transparent 45%),
             radial-gradient(ellipse at 90% 55%,rgba(150,190,70,.45),transparent 40%),
             radial-gradient(ellipse at 55% 20%,rgba(230,230,225,.25),transparent 50%)}
.topbar{position:absolute;left:0;top:0;width:1200px;height:79px;background:rgba(20,20,20,.75)}
.brand{position:absolute;display:flex;align-items:center;gap:9px;color:#fff;font-weight:400}
.brand .mark{width:36px;height:36px;border-radius:50%;background:var(--orange)}
.brand span{font-size:30px;letter-spacing:.5px}
.nav a{position:absolute;top:30px;color:#fff;font-size:13px;text-decoration:none;text-transform:uppercase;letter-spacing:.3px}
.btn{position:absolute;display:flex;align-items:center;justify-content:center;color:#fff;text-transform:uppercase;font-weight:700;border-radius:2px;letter-spacing:.4px}
.btn-contact{left:953px;top:19px;width:129px;height:37px;background:var(--orange);font-size:13px}
.hero-title{position:absolute;left:0;top:128px;width:1200px;text-align:center;color:#fff;font-size:46px;font-weight:300;letter-spacing:1.5px}
.hero-sub{position:absolute;left:0;top:196px;width:1200px;text-align:center;color:#fff;font-size:15px;font-weight:700;letter-spacing:.8px}
.btn-start{left:489px;top:253px;width:204px;height:48px;background:linear-gradient(#66bd33,var(--green-dark));font-size:17px;border-radius:3px}

/* app dashboard */
.app-frame{position:absolute;overflow:hidden;box-shadow:0 0 10px rgba(0,0,0,.25)}
.app{position:relative;width:920px;height:592px;background:var(--app-bg);font-size:9px;color:#555}
.app-top{position:absolute;left:0;top:0;width:920px;height:31px;background:var(--app-blue)}
.app-brand{position:absolute;left:8px;top:6px;display:flex;align-items:center;gap:5px;color:#fff;font-size:15px}
.app-brand i{width:18px;height:18px;border-radius:50%;background:var(--orange);display:block}
.app-search{position:absolute;left:627px;top:7px;width:160px;height:18px;background:#fff;border-radius:2px;color:#aaa;font-size:8px;padding:4px 6px}
.app-user{position:absolute;left:812px;top:5px;display:flex;align-items:center;gap:5px;color:#fff;font-size:8px}
.app-user i{width:20px;height:20px;border-radius:50%;background:#cfd8e3;display:block}
.app-side{position:absolute;left:0;top:31px;width:126px;height:561px;background:var(--app-side)}
.app-side .ico{position:absolute;left:0;top:0;width:32px;height:561px;background:var(--app-side-dark)}
.app-side .item{position:absolute;left:0;width:126px;height:30px;color:#c7ccd3;font-size:8px;padding:10px 0 0 42px;border-bottom:1px solid rgba(255,255,255,.04)}
.app-side .item b{position:absolute;left:11px;top:10px;width:10px;height:10px;border:1px solid #6f7984;border-radius:2px}
.app-side .item.active{background:var(--app-blue-dark);color:#fff;font-weight:700}
.app-side .item.active b{border-color:#fff}
.app-crumb{position:absolute;left:144px;top:45px;width:661px;height:19px;background:#fff;font-size:8px;padding:5px 8px;color:#666}
.stat{position:absolute;top:75px;height:41px;width:152px;background:#fff;border:1px solid #dde1e5;display:flex;align-items:center;gap:7px;padding-left:12px}
.stat .num{font-size:21px;color:#555;font-weight:300}
.stat .lbl{font-size:8px;color:#777}
.stat svg{width:20px;height:20px}
.panel{position:absolute;background:#fff;border:1px solid #dde1e5}
.report{left:140px;top:127px;width:156px;height:210px;background:var(--app-blue)}
.report .hd{height:24px;background:#26496f;color:#fff;font-size:10px;padding:6px 5px}
.report .row{display:flex;justify-content:space-between;height:23px;padding:6px 6px;color:#fff;font-size:9px;border-bottom:1px solid rgba(255,255,255,.15)}
.report .row:nth-child(even){background:#4b97e0}
.chart{left:311px;top:127px;width:494px;height:210px}
.box-hd{height:22px;border-bottom:1px solid #e6e6e6;display:flex;justify-content:space-between;align-items:center;padding:0 8px;font-size:8px;font-weight:700;color:#333}
.box-hd em{font-style:normal;font-weight:400;color:#333}
.list{padding:4px 8px}
.list p{font-size:7px;color:#666;line-height:14px;border-bottom:1px dotted #e4e4e4;display:flex;justify-content:space-between;align-items:center}
.list p s{text-decoration:none;display:inline-block;width:26px;height:6px}
.notif{left:140px;top:352px;width:328px;height:92px}
.tasks{left:483px;top:352px;width:322px;height:92px}
.coll{left:140px;top:455px;width:328px;height:120px}
.asse{left:483px;top:455px;width:322px;height:120px}
.tbl{padding:4px 8px;font-size:7px}
.tbl .th{display:flex;justify-content:space-between;background:#3f8bd6;color:#fff;padding:3px 5px}
.tbl .tr{display:flex;justify-content:space-between;padding:3px 5px;border-bottom:1px solid #eee}
.tbl .mini{float:right;margin-top:8px;background:var(--orange);color:#fff;padding:2px 6px;font-size:7px}

/* discover */
.h2{position:absolute;left:0;width:1200px;text-align:center;font-size:30px;font-weight:400;letter-spacing:1px;color:#333}
.tabs{position:absolute;left:208px;top:882px;width:792px;height:63px;display:flex;border:1px solid var(--line);background:#f3f3f3}
.tab{flex:1;display:flex;align-items:center;justify-content:center;gap:12px;font-size:16px;color:#555;border-right:1px solid var(--line)}
.tab:last-child{border-right:none}
.tab.active{background:#fff;border-bottom:3px solid var(--orange)}
.tab svg{width:28px;height:28px}
.feature-title{position:absolute;left:152px;top:1050px;font-size:24px;color:#222}
.feature-text{position:absolute;left:152px;top:1096px;width:300px;font-size:14px;line-height:24px;color:#999}
.btn-more{left:152px;top:1211px;width:153px;height:40px;background:var(--orange);font-size:15px}

/* secure */
.secure{position:absolute;left:0;top:1348px;width:1200px;height:415px;background:var(--grey-band)}
.ring{position:absolute;width:90px;height:90px;border-radius:50%;border:2px solid;display:flex;align-items:center;justify-content:center;background:#fff}
.ring svg{width:46px;height:46px}
.sec-title{position:absolute;width:300px;text-align:center;font-size:21px;color:#444}
.sec-text{position:absolute;width:300px;text-align:center;font-size:14px;line-height:24px;color:#999}

/* three columns */
.col-title{position:absolute;top:1808px;font-size:21px;color:#222}
.video{position:absolute;left:144px;top:1874px;width:296px;height:168px;
  background:linear-gradient(135deg,#2f3a44 0%,#6e7a82 45%,#d9d6cf 75%,#8a7d70 100%)}
.video .bar{position:absolute;left:0;bottom:0;width:296px;height:14px;background:rgba(0,0,0,.7)}
.video .bar i{position:absolute;left:30px;top:6px;width:240px;height:2px;background:#777}
.video .bar b{position:absolute;left:30px;top:6px;width:50px;height:2px;background:#d32}
.magic{position:absolute;left:479px;top:1858px;width:272px;font-size:14px;line-height:24px;color:#999}
.magic .art{float:right;width:94px;height:126px;margin:0 0 4px 10px;
  background:radial-gradient(circle at 50% 45%,#f08a2a 0%,#d9452f 30%,#6c4aa5 55%,#2a9bd8 75%,#fff 90%)}
.bullets{position:absolute;left:797px;top:1864px;list-style:none}
.bullets li{font-size:17px;color:#555;height:33.5px;padding-left:22px;position:relative}
.bullets li:before{content:"";position:absolute;left:2px;top:7px;width:7px;height:7px;border-radius:50%;background:#777}
.quote{position:absolute;left:797px;top:1974px;font-size:19px;color:var(--orange);font-weight:700}

/* partners */
.partners{position:absolute;left:234px;top:2112px;width:730px;height:106px;border-top:1px solid #eee;border-bottom:1px solid #eee}
.badge{position:absolute;top:26px;height:52px;border-radius:4px;background:#e4e4e4}
.arrow{position:absolute;top:2146px;width:38px;height:38px;border-radius:50%;background:#ddd;display:flex;align-items:center;justify-content:center}

/* cta */
.cta{position:absolute;left:0;top:2241px;width:1200px;height:116px;background:var(--orange)}
.cta-text{position:absolute;left:258px;top:41px;font-size:28px;color:#fff;font-weight:400;letter-spacing:.5px}
.cta-text b{font-weight:900}
.btn-cta{left:698px;top:39px;width:193px;height:39px;background:var(--brown);font-size:15px;font-weight:400}

/* footer */
.footer{position:absolute;left:0;top:2357px;width:1200px;height:378px;background:var(--footer);color:var(--footer-text)}
.f-h{position:absolute;top:44px;font-size:13px;font-weight:700;color:#fff;letter-spacing:.5px;text-transform:uppercase}
.f-list{position:absolute;top:84px;list-style:none}
.f-list li{font-size:13px;height:26px}
.f-div{position:absolute;top:0;width:1px;height:378px;background:#444}
.social li{display:flex;align-items:center;gap:14px;height:31px;font-size:13px}
.social i{width:20px;height:20px;border-radius:50%;background:#e4e4e4;display:block}
.news-in{position:absolute;left:507px;top:2650px;width:198px;height:34px;background:#e8e8e8;border-radius:2px 0 0 2px}
.news-in i{position:absolute;left:10px;top:12px;width:14px;height:10px;background:#999}
.news-btn{position:absolute;left:705px;top:2650px;width:74px;height:34px;background:var(--green);color:#fff;font-size:14px;display:flex;align-items:center;justify-content:center}
.bottom{position:absolute;left:0;top:2735px;width:1200px;height:73px;background:var(--footer-bottom);color:#ccc;font-size:12px}
</style>
</head>
<body>
<div class="page">

  <!-- HERO -->
  <section class="hero">
    <div class="hero-photo" role="img" aria-label="Blurred photo of a bright modern office with people at work"></div>
    <header class="topbar">
      <div class="brand" style="left:120px;top:21px"><i class="mark"></i><span>Tavelo</span></div>
      <nav class="nav">
        <a style="left:314px">Home</a>
        <a style="left:384px">How it works</a>
        <a style="left:507px">CRM</a>
        <a style="left:567px">About</a>
        <a style="left:640px">Partners</a>
      </nav>
      <div class="btn btn-contact">Contact us</div>
    </header>
    <h1 class="hero-title">Assessment Made Simple</h1>
    <p class="hero-sub">THE BEST ENGAGEMENT PLATFORM TO DELIVER SAAS SOLUTION.</p>
    <div class="btn btn-start">Get started</div>

    <div class="app-frame" style="left:140px;top:341px;width:920px;height:415px">
      <div class="app">
        <div class="app-top">
          <div class="app-brand"><i></i>Tavelo</div>
          <div class="app-search">Search</div>
          <div class="app-user"><i></i>Torlak Brennvik ▾</div>
        </div>
        <div class="app-side"><div class="ico"></div>
          <div class="item active" style="top:0"><b></b>Dashboard</div>
          <div class="item" style="top:30px"><b></b>My Library</div>
          <div class="item" style="top:60px"><b></b>Assessment</div>
          <div class="item" style="top:90px"><b></b>Schedule</div>
          <div class="item" style="top:120px"><b></b>Marking</div>
          <div class="item" style="top:150px"><b></b>Reports</div>
          <div class="item" style="top:180px"><b></b>Admin</div>
        </div>
        <div class="app-crumb">You are here: ⌂</div>
        <div class="stat" style="left:142px"><svg viewBox="0 0 20 20"><path d="M10 3 18 7 10 11 2 7Z M2 10 10 14 18 10 M2 13 10 17 18 13" fill="none" stroke="#e8603c" stroke-width="1.4"/></svg><span class="num">36</span><span class="lbl">Collections</span></div>
        <div class="stat" style="left:311px"><svg viewBox="0 0 20 20"><path d="M3 17 15 5 17 7 5 19Z" fill="none" stroke="#3f8bd6" stroke-width="1.4"/></svg><span class="num">12</span><span class="lbl">Assessments</span></div>
        <div class="stat" style="left:481px"><svg viewBox="0 0 20 20"><circle cx="10" cy="10" r="6" fill="none" stroke="#f2b233" stroke-width="1.6"/></svg><span class="num">48</span><span class="lbl">Tasks</span></div>
        <div class="stat" style="left:655px"><svg viewBox="0 0 20 20"><path d="M2 15 8 9 12 12 18 5" fill="none" stroke="#2db3a6" stroke-width="1.6"/></svg><span class="num">76%</span><span class="lbl">Average</span></div>
        <div class="panel report">
          <div class="hd">Percentage report</div>
          <div class="row"><span>Science</span><span>49 %</span></div>
          <div class="row"><span>Maths</span><span>56 %</span></div>
          <div class="row"><span>History</span><span>38 %</span></div>
          <div class="row"><span>Biology</span><span>52 %</span></div>
          <div class="row"><span>English</span><span>34 %</span></div>
          <div class="row"><span>Java 101</span><span>20 %</span></div>
          <div class="row"><span>Philosophy</span><span>8 %</span></div>
        </div>
        <div class="panel chart">
          <svg width="494" height="210" viewBox="0 0 494 210" font-family="Lato, sans-serif" font-size="7" fill="#666">
            <g stroke="#eee"><line x1="45" y1="40" x2="470" y2="40"/><line x1="45" y1="73" x2="470" y2="73"/><line x1="45" y1="106" x2="470" y2="106"/><line x1="45" y1="139" x2="470" y2="139"/><line x1="45" y1="172" x2="470" y2="172"/></g>
            <text x="28" y="42">80</text><text x="28" y="75">60</text><text x="28" y="108">40</text><text x="28" y="141">20</text><text x="30" y="174">0</text>
            <polyline points="80,91 130,80 185,109 240,86 295,116 350,139 405,159" fill="none" stroke="var(--teal)" stroke-width="1.6"/>
            <g fill="#fff" stroke="var(--teal)" stroke-width="1.4"><circle cx="80" cy="91" r="2.5"/><circle cx="130" cy="80" r="2.5"/><circle cx="185" cy="109" r="2.5"/><circle cx="240" cy="86" r="2.5"/><circle cx="295" cy="116" r="2.5"/><circle cx="350" cy="139" r="2.5"/><circle cx="405" cy="159" r="2.5"/></g>
            <rect x="117" y="62" width="26" height="12" fill="#333"/><text x="122" y="70" fill="#fff">56 %</text>
            <text x="68" y="192">Science</text><text x="121" y="192">Maths</text><text x="173" y="192">History</text><text x="228" y="192">Biology</text><text x="283" y="192">English</text><text x="341" y="192">Java</text><text x="390" y="192">Philosophy</text>
          </svg>
        </div>
        <div class="panel notif">
          <div class="box-hd"><span>NOTIFICATIONS</span><em>Show All ▸</em></div>
          <div class="list">
            <p>Ann Berg shared Collection Biology 101</p>
            <p>Status of Collection Harbor set to ready</p>
            <p>New questions in Collection Maths</p>
            <p>Review ready for English exam</p>
          </div>
        </div>
        <div class="panel tasks">
          <div class="box-hd"><span>TASKS</span><em>Show All ▸</em></div>
          <div class="list">
            <p>Test Physics 102 ready to schedule<s style="background:var(--orange)"></s></p>
            <p>Biology ready to be marked<s style="background:#e04a3a"></s></p>
            <p>Chemistry quiz ready to review<s style="background:var(--orange)"></s></p>
            <p>History test needs questions<s style="background:var(--green)"></s></p>
          </div>
        </div>
        <div class="panel coll">
          <div class="box-hd"><span>MY COLLECTIONS</span><em>Show All ▸</em></div>
          <div class="tbl">
            <div class="th"><span>Name</span><span>Last Updated</span></div>
            <div class="tr"><span>Harbor</span><span>12 March 2013</span></div>
            <div class="tr"><span>Biology</span><span>21 August 2013</span></div>
            <span class="mini">New Collection</span>
          </div>
        </div>
        <div class="panel asse">
          <div class="box-hd"><span>MY ASSESSMENTS</span><em>Show All ▸</em></div>
          <div class="tbl">
            <div class="th"><span>Name</span><span>Last Updated</span></div>
            <div class="tr"><span>English 101</span><span>11 March 2013</span></div>
            <div class="tr"><span>Maths</span><span>14 August 2013</span></div>
            <span class="mini">New Assessment</span>
          </div>
        </div>
      </div>
    </div>
  </section>

  <!-- DISCOVER -->
  <h2 class="h2" style="top:806px">Discover how Tavelo can help You</h2>
  <div class="tabs">
    <div class="tab active"><svg viewBox="0 0 28 28"><rect x="3" y="5" width="22" height="15" fill="none" stroke="#444" stroke-width="1.5"/><path d="M7 16 12 11 15 14 21 8 M10 20 7 25 M18 20 21 25" fill="none" stroke="var(--orange)" stroke-width="1.5"/></svg>Education users</div>
    <div class="tab"><svg viewBox="0 0 28 28"><rect x="3" y="6" width="22" height="16" fill="none" stroke="var(--orange)" stroke-width="1.5"/><path d="M6 19 11 13 15 17 22 10" fill="none" stroke="#444" stroke-width="1.5"/></svg>Corporate users</div>
    <div class="tab"><svg viewBox="0 0 28 28"><circle cx="13" cy="12" r="8" fill="none" stroke="#444" stroke-width="1.5"/><circle cx="13" cy="12" r="3" fill="var(--orange)"/><path d="M10 20 10 25 M16 20 16 25" stroke="#444" stroke-width="1.5"/></svg>CRM integration</div>
    <div class="tab"><svg viewBox="0 0 28 28"><path d="M6 3 H18 L22 7 V25 H6Z" fill="none" stroke="#444" stroke-width="1.5"/><circle cx="19" cy="20" r="5" fill="var(--orange)"/></svg>Our Approach</div>
  </div>
  <h3 class="feature-title">Education users</h3>
  <p class="feature-text">Lorem Ipsum is simply dummy text of the printing and typesetting industry. Lorem Ipsum has been the industry's standard dummy text ever since the 1500s.</p>
  <div class="btn btn-more">Read more</div>

  <div class="app-frame" style="left:515px;top:1000px;width:541px;height:348px">
    <div class="app" style="transform:scale(.588);transform-origin:0 0">
      <div class="app-top">
        <div class="app-brand"><i></i>Tavelo</div>
        <div class="app-search">Search</div>
        <div class="app-user"><i></i>Torlak Brennvik ▾</div>
      </div>
      <div class="app-side"><div class="ico"></div>
        <div class="item active" style="top:0"><b></b>Dashboard</div>
        <div class="item" style="top:30px"><b></b>My Library</div>
        <div class="item" style="top:60px"><b></b>Assessment</div>
        <div class="item" style="top:90px"><b></b>Schedule</div>
        <div class="item" style="top:120px"><b></b>Marking</div>
        <div class="item" style="top:150px"><b></b>Reports</div>
        <div class="item" style="top:180px"><b></b>Admin</div>
      </div>
      <div class="app-crumb">You are here: ⌂</div>
      <div class="stat" style="left:142px"><svg viewBox="0 0 20 20"><path d="M10 3 18 7 10 11 2 7Z M2 10 10 14 18 10 M2 13 10 17 18 13" fill="none" stroke="#e8603c" stroke-width="1.4"/></svg><span class="num">36</span><span class="lbl">Collections</span></div>
      <div class="stat" style="left:311px"><svg viewBox="0 0 20 20"><path d="M3 17 15 5 17 7 5 19Z" fill="none" stroke="#3f8bd6" stroke-width="1.4"/></svg><span class="num">12</span><span class="lbl">Assessments</span></div>
      <div class="stat" style="left:481px"><svg viewBox="0 0 20 20"><circle cx="10" cy="10" r="6" fill="none" stroke="#f2b233" stroke-width="1.6"/></svg><span class="num">48</span><span class="lbl">Tasks</span></div>
      <div class="stat" style="left:655px"><svg viewBox="0 0 20 20"><path d="M2 15 8 9 12 12 18 5" fill="none" stroke="#2db3a6" stroke-width="1.6"/></svg><span class="num">76%</span><span class="lbl">Average</span></div>
      <div class="panel report">
        <div class="hd">Percentage report</div>
        <div class="row"><span>Science</span><span>49 %</span></div>
        <div class="row"><span>Maths</span><span>56 %</span></div>
        <div class="row"><span>History</span><span>38 %</span></div>
        <div class="row"><span>Biology</span><span>52 %</span></div>
        <div class="row"><span>English</span><span>34 %</span></div>
        <div class="row"><span>Java 101</span><span>20 %</span></div>
        <div class="row"><span>Philosophy</span><span>8 %</span></div>
      </div>
      <div class="panel chart">
        <svg width="494" height="210" viewBox="0 0 494 210" font-family="Lato, sans-serif" font-size="7" fill="#666">
          <g stroke="#eee"><line x1="45" y1="40" x2="470" y2="40"/><line x1="45" y1="73" x2="470" y2="73"/><line x1="45" y1="106" x2="470" y2="106"/><line x1="45" y1="139" x2="470" y2="139"/><line x1="45" y1="172" x2="470" y2="172"/></g>
          <polyline points="80,91 130,80 185,109 240,86 295,116 350,139 405,159" fill="none" stroke="var(--teal)" stroke-width="1.6"/>
          <g fill="#fff" stroke="var(--teal)" stroke-width="1.4"><circle cx="80" cy="91" r="2.5"/><circle cx="130" cy="80" r="2.5"/><circle cx="185" cy="109" r="2.5"/><circle cx="240" cy="86" r="2.5"/><circle cx="295" cy="116" r="2.5"/><circle cx="350" cy="139" r="2.5"/><circle cx="405" cy="159" r="2.5"/></g>
          <rect x="117" y="62" width="26" height="12" fill="#333"/><text x="122" y="70" fill="#fff">56 %</text>
          <text x="68" y="192">Science</text><text x="121" y="192">Maths</text><text x="173" y="192">History</text><text x="228" y="192">Biology</text><text x="283" y="192">English</text><text x="341" y="192">Java</text><text x="390" y="192">Philosophy</text>
        </svg>
      </div>
      <div class="panel notif">
        <div class="box-hd"><span>NOTIFICATIONS</span><em>Show All ▸</em></div>
        <div class="list"><p>Ann Berg shared Collection Biology 101</p><p>Status of Collection Harbor set to ready</p><p>New questions in Collection Maths</p><p>Review ready for English exam</p></div>
      </div>
      <div class="panel tasks">
        <div class="box-hd"><span>TASKS</span><em>Show All ▸</em></div>
        <div class="list"><p>Test Physics 102 ready to schedule<s style="background:var(--orange)"></s></p><p>Biology ready to be marked<s style="background:#e04a3a"></s></p><p>Chemistry quiz ready to review<s style="background:var(--orange)"></s></p><p>History test needs questions<s style="background:var(--green)"></s></p></div>
      </div>
      <div class="panel coll">
        <div class="box-hd"><span>MY COLLECTIONS</span><em>Show All ▸</em></div>
        <div class="tbl"><div class="th"><span>Name</span><span>Last Updated</span></div><div class="tr"><span>Harbor</span><span>12 March 2013</span></div><div class="tr"><span>Biology</span><span>21 August 2013</span></div><span class="mini">New Collection</span></div>
      </div>
      <div class="panel asse">
        <div class="box-hd"><span>MY ASSESSMENTS</span><em>Show All ▸</em></div>
        <div class="tbl"><div class="th"><span>Name</span><span>Last Updated</span></div><div class="tr"><span>English 101</span><span>11 March 2013</span></div><div class="tr"><span>Maths</span><span>14 August 2013</span></div><span class="mini">New Assessment</span></div>
      </div>
    </div>
  </div>

  <!-- SECURE -->
  <section class="secure">
    <h2 class="h2" style="top:57px">Secure Your Software</h2>
    <div class="ring" style="left:241px;top:138px;border-color:var(--orange)"><svg viewBox="0 0 46 46"><rect x="6" y="26" width="7" height="12" fill="none" stroke="var(--orange)" stroke-width="2"/><rect x="19" y="18" width="7" height="20" fill="none" stroke="var(--orange)" stroke-width="2"/><rect x="32" y="22" width="7" height="16" fill="none" stroke="var(--orange)" stroke-width="2"/><path d="M9 20 22 10 36 15" fill="none" stroke="var(--orange)" stroke-width="2"/></svg></div>
    <div class="ring" style="left:550px;top:138px;border-color:var(--green)"><svg viewBox="0 0 46 46"><path d="M10 36 32 12 M14 12 36 34 M28 8 38 18 M8 28 18 38" fill="none" stroke="var(--green)" stroke-width="3" stroke-linecap="round"/></svg></div>
    <div class="ring" style="left:863px;top:138px;border-color:var(--app-blue)"><svg viewBox="0 0 46 46"><ellipse cx="23" cy="10" rx="13" ry="5" fill="none" stroke="var(--app-blue)" stroke-width="2"/><path d="M10 10 V36 C10 43 36 43 36 36 V10 M10 19 C10 26 36 26 36 19 M10 28 C10 35 36 35 36 28" fill="none" stroke="var(--app-blue)" stroke-width="2"/></svg></div>
    <h3 class="sec-title" style="left:136px;top:250px">Network Protection</h3>
    <h3 class="sec-title" style="left:445px;top:250px">Enduser Protection</h3>
    <h3 class="sec-title" style="left:758px;top:250px">Server Protection</h3>
    <p class="sec-text" style="left:136px;top:293px">Lorem Ipsum is simply dummy text<br>of the printing and typesetting.</p>
    <p class="sec-text" style="left:445px;top:293px">Lorem Ipsum is simply dummy text<br>of the printing and typesetting.</p>
    <p class="sec-text" style="left:758px;top:293px">Lorem Ipsum is simply dummy text<br>of the printing and typesetting.</p>
  </section>

  <!-- THREE COLUMNS -->
  <h3 class="col-title" style="left:140px">Thats Me</h3>
  <h3 class="col-title" style="left:477px">Three is Magic Number</h3>
  <h3 class="col-title" style="left:797px">Field Team Approach</h3>
  <div class="video" role="img" aria-label="Video still of two colleagues in a business meeting"><div class="bar"><i></i><b></b></div></div>
  <div class="magic"><div class="art" role="img" aria-label="Colourful illustration of people joined in a circle"></div>Lorem Ipsum is the end simply dummy text of the printing and typesetting industry. Lorem Ipsum has Lorem Ipsum is the end simply dummy text of the printing and typesetting.</div>
  <ul class="bullets"><li>No Servers</li><li>No Maintainence</li><li>No Worries</li></ul>
  <p class="quote">“Assessment Made Simple”</p>

  <!-- PARTNERS -->
  <div class="arrow" style="left:164px"><svg width="14" height="14" viewBox="0 0 14 14"><path d="M9 2 4 7 9 12" fill="none" stroke="#fff" stroke-width="2"/></svg></div>
  <div class="partners">
    <div class="badge" style="left:12px;width:150px"></div>
    <div class="badge" style="left:200px;width:150px"></div>
    <div class="badge" style="left:380px;width:150px"></div>
    <div class="badge" style="left:570px;width:150px"></div>
  </div>
  <div class="arrow" style="left:992px"><svg width="14" height="14" viewBox="0 0 14 14"><path d="M5 2 10 7 5 12" fill="none" stroke="#fff" stroke-width="2"/></svg></div>

  <!-- CTA -->
  <section class="cta">
    <p class="cta-text">Try Tavelo risk-free for <b>30</b> days</p>
    <div class="btn btn-cta">Get started</div>
  </section>

  <!-- FOOTER -->
  <footer class="footer">
    <h4 class="f-h" style="left:142px">Sitemap</h4>
    <ul class="f-list" style="left:144px"><li>Tour</li><li>Pricing</li><li>Free Trial</li><li>About Us</li><li>Customer Stories</li><li>Testimonials</li><li>Partners</li><li>Contact Us</li></ul>
    <h4 class="f-h" style="left:320px">Services</h4>
    <ul class="f-list" style="left:322px"><li>Psd to Html</li><li>CRM</li><li>Responsive</li><li>Forums</li><li>Blogs</li><li>Mobile</li><li>Softwares</li></ul>
    <div class="f-div" style="left:447px"></div>
    <h4 class="f-h" style="left:507px">We are social</h4>
    <ul class="f-list social" style="left:507px;top:90px"><li><i></i>Follow us on Chirper</li><li><i></i>Circle us on Orbit</li><li><i></i>Like Us on Friendhub</li><li><i></i>Follow Us on Linkwork</li></ul>
    <h4 class="f-h" style="left:507px;top:230px">Subscribe to newsletter</h4>
    <p class="abs" style="left:507px;top:263px;font-size:13px">Enter your email and subscribe.</p>
    <div class="f-div" style="left:822px"></div>
    <h4 class="f-h" style="left:869px">Our contact</h4>
    <ul class="f-list" style="left:869px;top:86px"><li style="height:28px;font-size:14px">Tavelo.com</li><li style="height:28px;font-size:14px">48 Alder Row, Ste 310</li><li style="height:28px;font-size:14px">Marrow Bay, QX 40517</li><li style="height:28px;font-size:14px">555-014-2290 x1</li><li style="height:28px;font-size:14px">sales@Tavelo.com</li></ul>
  </footer>
  <div class="news-in"><i></i></div>
  <div class="news-btn">Submit</div>

  <div class="bottom">
    <div class="brand" style="left:142px;top:20px"><i class="mark" style="width:30px;height:30px"></i><span style="font-size:26px">Tavelo</span></div>
    <p class="abs" style="left:285px;top:29px">Terms of Service &nbsp;&nbsp;|&nbsp;&nbsp; Privacy Policy &nbsp;&nbsp;|&nbsp;&nbsp; SiteMap</p>
    <p class="abs" style="left:842px;top:29px">copyright2014.Tavelo. All Rights Reserved</p>
  </div>
</div>
</body>
</html>
```